Grafik für Bibliothek
Zielgruppe
Anselm-Dreyhaupt-Bibliothek für Wandelstudien. Gemeinnütziger Verein, gegründet von Anselm Dreyhaupt (Freier Ehrenring Wessling). Im Interesse der Zivilgesellschaft. Schwerunkt Zukunftsdebatten.
Aufgabenstellung
Die Grafik steht am Ende einer Studie, die in einem Szenarioprozess einen 'Zukunftsraum' skizziert.
Vier Szenarios sind entstanden. Zwischen diesen spannt sich der Zukunftsraum auf. (Texte der Szeanrios anbei)
Die Szenarios basieren auf vielen Szenarienbündel, die geclustert als Punkte dargestellt sind. Diese vielen Punkte sind an sich nicht wichtig in der Darstellung, da sie zu einem Szenario verdichtet werden. Sie zeigen aber die Distanz zu den anderen Szenarien und einen methodischen Schritt an.
Diese unterscheiden sind an zwei Achsen. (Benennung anbei)
Die Szenarios sind unterschiedlich realistisch, das sollte grafisch sichtbar werden (in Vorlage - nicht gut - als Pfeile). (Bewertung in xx Punkten von 9 = sehr wahrscheinlich)
Die Grafik muss auf einer Powerpoint-Folie präsentierbar sein.
Logo der ADB

```html
<!DOCTYPE html>
<html lang="de">
<head>
<meta charset="utf-8">
<title>Zukunftsraum Salzburg 2040</title>
<link href="https://fonts.googleapis.com/css2?family=Outfit:wght@300;400;600;700;800&display=swap" rel="stylesheet">
<style>
  :root {
    --bg: #fafafa;
    --ink: #111111;
    --muted: #8a8a8a;
    --axis: #e6e6e6;
    --axis-dot: #e9e9e9;
    --s1: #d08b4e;
    --s2: #5d3b58;
    --s3: #9c8399;
    --s4: #d4aa8e;
    --ring: #fafafa;
  }
  html, body {
    margin: 0;
    padding: 0;
    width: 1200px;
    height: 777px;
    overflow: hidden;
    background: var(--bg);
  }
  .future-space {
    display: block;
    width: 1200px;
    height: 777px;
    font-family: "Outfit", "Helvetica Neue", Arial, sans-serif;
  }
  .title { font-size: 37px; fill: var(--ink); letter-spacing: -0.3px; }
  .title-strong { font-weight: 800; }
  .title-light { font-weight: 300; }

  .axis-line { fill: none; stroke: var(--axis); stroke-width: 2; }
  .axis-end { fill: var(--axis-dot); }
  .axis-label { font-size: 16px; font-weight: 700; fill: var(--ink); }

  .cluster circle { stroke: var(--ring); stroke-width: 1.5; }
  .cluster-1 circle { fill: var(--s1); }
  .cluster-2 circle { fill: var(--s2); }
  .cluster-3 circle { fill: var(--s3); }
  .cluster-4 circle { fill: var(--s4); }

  .scenario-kicker { font-size: 14px; font-weight: 700; }
  .scenario-number { font-size: 14px; font-weight: 700; fill: #ffffff; }
  .scenario-text { font-size: 13px; font-weight: 300; fill: var(--muted); }
  .scenario-prob { font-size: 13px; font-weight: 400; fill: var(--ink); }
  .scenario-prob tspan.value { font-weight: 700; }

  .scenario-1 .scenario-kicker { fill: var(--s1); }
  .scenario-1 .badge { fill: var(--s1); }
  .scenario-2 .scenario-kicker { fill: var(--s2); }
  .scenario-2 .badge { fill: var(--s2); }
  .scenario-3 .scenario-kicker { fill: var(--s3); }
  .scenario-3 .badge { fill: var(--s3); }
  .scenario-4 .scenario-kicker { fill: var(--s4); }
  .scenario-4 .badge { fill: var(--s4); }
</style>
</head>
<body>
<svg class="future-space" viewBox="0 0 1200 777" xmlns="http://www.w3.org/2000/svg" role="img" aria-label="Zukunftsraum Salzburg 2040: vier Szenarien zwischen zwei Achsen">

  <text class="title" x="600" y="80" text-anchor="middle"><tspan class="title-strong">Zukunftsraum</tspan><tspan class="title-light"> Salzburg 2040</tspan></text>

  <!-- Achsen -->
  <g class="axes">
    <path class="axis-line" d="M755 201 Q 615 430 670 705"/>
    <path class="axis-line" d="M307 428 Q 560 370 938 528"/>
    <circle class="axis-end" cx="755" cy="201" r="6.5"/>
    <circle class="axis-end" cx="670" cy="705" r="6.5"/>
    <circle class="axis-end" cx="307" cy="428" r="6.5"/>
    <circle class="axis-end" cx="938" cy="528" r="6.5"/>

    <text class="axis-label" x="680" y="163">Weiterentwicklung</text>
    <text class="axis-label" x="680" y="184">der bestehenden Konflikte</text>
    <text class="axis-label" x="292" y="423" text-anchor="end">Moderate</text>
    <text class="axis-label" x="292" y="444" text-anchor="end">Klimawandelauswirkungen</text>
    <text class="axis-label" x="955" y="524">Stark beschleunigter</text>
    <text class="axis-label" x="955" y="544">Klimawandel</text>
    <text class="axis-label" x="675" y="736" text-anchor="middle">Neue Konfliktlinien</text>
  </g>

  <!-- Szenarienbündel -->
  <g class="cluster cluster-4">
    <circle cx="433" cy="405" r="11"/><circle cx="438" cy="412" r="11"/><circle cx="527" cy="418" r="11"/>
    <circle cx="393" cy="452" r="11"/><circle cx="388" cy="463" r="11"/><circle cx="399" cy="460" r="11"/>
    <circle cx="392" cy="476" r="11"/><circle cx="397" cy="478" r="11"/>
    <circle cx="474" cy="450" r="11"/><circle cx="476" cy="462" r="11"/><circle cx="482" cy="464" r="11"/>
    <circle cx="512" cy="478" r="11"/><circle cx="515" cy="491" r="11"/><circle cx="512" cy="496" r="11"/>
    <circle cx="550" cy="474" r="11"/>
    <circle cx="424" cy="530" r="11"/><circle cx="432" cy="528" r="11"/><circle cx="420" cy="539" r="11"/>
    <circle cx="446" cy="540" r="11"/><circle cx="454" cy="530" r="11"/><circle cx="458" cy="546" r="11"/>
    <circle cx="451" cy="548" r="11"/>
    <circle cx="538" cy="533" r="11"/><circle cx="550" cy="540" r="11"/><circle cx="540" cy="540" r="11"/>
    <circle cx="602" cy="580" r="11"/><circle cx="588" cy="590" r="11"/><circle cx="572" cy="594" r="11"/>
    <circle cx="566" cy="605" r="11"/>
    <circle cx="448" cy="610" r="11"/><circle cx="440" cy="616" r="11"/><circle cx="442" cy="619" r="11"/>
    <circle cx="496" cy="613" r="11"/><circle cx="503" cy="617" r="11"/><circle cx="496" cy="622" r="11"/>
  </g>
  <g class="cluster cluster-1">
    <circle cx="455" cy="268" r="11"/><circle cx="460" cy="273" r="11"/><circle cx="476" cy="262" r="11"/>
    <circle cx="482" cy="268" r="11"/><circle cx="491" cy="272" r="11"/>
    <circle cx="545" cy="265" r="11"/><circle cx="540" cy="278" r="11"/><circle cx="562" cy="276" r="11"/>
    <circle cx="566" cy="284" r="11"/><circle cx="616" cy="312" r="11"/>
    <circle cx="437" cy="329" r="11"/><circle cx="440" cy="334" r="11"/>
    <circle cx="519" cy="340" r="11"/><circle cx="518" cy="345" r="11"/>
    <circle cx="557" cy="346" r="11"/><circle cx="570" cy="354" r="11"/>
    <circle cx="436" cy="388" r="11"/><circle cx="442" cy="392" r="11"/>
    <circle cx="527" cy="408" r="11"/><circle cx="548" cy="410" r="11"/>
  </g>
  <g class="cluster cluster-2">
    <circle cx="780" cy="340" r="11"/><circle cx="786" cy="346" r="11"/><circle cx="790" cy="354" r="11"/>
    <circle cx="797" cy="368" r="11"/><circle cx="822" cy="345" r="11"/><circle cx="826" cy="350" r="11"/>
    <circle cx="830" cy="358" r="11"/><circle cx="812" cy="384" r="11"/><circle cx="816" cy="390" r="11"/>
    <circle cx="788" cy="404" r="11"/>
  </g>
  <g class="cluster cluster-3">
    <circle cx="772" cy="534" r="11"/><circle cx="750" cy="557" r="11"/><circle cx="749" cy="562" r="11"/>
    <circle cx="754" cy="608" r="11"/><circle cx="743" cy="622" r="11"/>
  </g>

  <!-- Szenario-Beschreibungen -->
  <g class="scenario scenario-1">
    <text class="scenario-kicker" x="391" y="216" text-anchor="end">Szenario</text>
    <circle class="badge" cx="406" cy="211" r="11"/>
    <text class="scenario-number" x="406" y="216" text-anchor="middle">1</text>
    <text class="scenario-text" x="416" y="239" text-anchor="end">Weiter so.</text>
    <text class="scenario-text" x="416" y="257" text-anchor="end">Ein erfolgreiches Salzburg</text>
    <text class="scenario-text" x="416" y="275" text-anchor="end">mit schwelenden Krisen</text>
    <text class="scenario-prob" x="416" y="294" text-anchor="end">Wahrscheinlichkeit: <tspan class="value">5,4 von 9</tspan></text>
  </g>
  <g class="scenario scenario-2">
    <text class="scenario-kicker" x="867" y="328">Szenario</text>
    <circle class="badge" cx="939" cy="323" r="11"/>
    <text class="scenario-number" x="939" y="328" text-anchor="middle">2</text>
    <text class="scenario-text" x="867" y="352">„Ellenbogen raus“ in der Krise.</text>
    <text class="scenario-text" x="867" y="370">Ein Salzburg, das in der Klimakrise</text>
    <text class="scenario-text" x="867" y="388">mit sich selbst ringt</text>
    <text class="scenario-prob" x="867" y="408">Wahrscheinlichkeit: <tspan class="value">6,1 von 9</tspan></text>
  </g>
  <g class="scenario scenario-3">
    <text class="scenario-kicker" x="802" y="593">Szenario</text>
    <circle class="badge" cx="876" cy="588" r="11"/>
    <text class="scenario-number" x="876" y="593" text-anchor="middle">3</text>
    <text class="scenario-text" x="802" y="616">Zusammenstehen in der Krise.</text>
    <text class="scenario-text" x="802" y="634">Ein Salzburg, das in der Krise</text>
    <text class="scenario-text" x="802" y="652">zusammenrückt</text>
    <text class="scenario-prob" x="802" y="671">Wahrscheinlichkeit: <tspan class="value">4,2 von 9</tspan></text>
  </g>
  <g class="scenario scenario-4">
    <text class="scenario-kicker" x="375" y="589" text-anchor="end">Szenario</text>
    <circle class="badge" cx="390" cy="584" r="11"/>
    <text class="scenario-number" x="390" y="589" text-anchor="middle">4</text>
    <text class="scenario-text" x="402" y="612" text-anchor="end">Umbau mit Konflikten.</text>
    <text class="scenario-text" x="402" y="630" text-anchor="end">Ein sich erneuerndes Salzburg,</text>
    <text class="scenario-text" x="402" y="648" text-anchor="end">das den Gegenwind spürt</text>
    <text class="scenario-prob" x="402" y="667" text-anchor="end">Wahrscheinlichkeit: <tspan class="value">5,0 von 9</tspan></text>
  </g>
</svg>
</body>
</html>
```